Music Industry Business Needs a Business Card Design

Copper Lantern is an audio mastering company that has been in business for 20 years. Mastering is the final creative step in the music production chain. Our job is to make the music sound as good as it possibly can prior to release to the public. Our world is technical, artistic, precise. We work on everything from independent artists to the music for the Grandfield Cup. We are looking for a new, more modern business card design. I am uploading a copy of our logo, although it doesn't absolutely need to be included in the design.

Target Market(s)

Music Industry Professionals

Industry/Entity Type

Business

Contact Information for Business Card

Address, Phone, Email, Website, Name, Job Title

Font styles to use
Sans Serif

Requirements
Must have
• Sorry, but I don't have any concrete things to request. If I had a clear idea of what I want, I would probably just design something myself. I am looking for fresh input and thought I would try this.
Should not have
• Anything that is typical, such as headphones or the like.

```html
<!DOCTYPE html>
<html lang="en">
<head>
<meta charset="utf-8">
<title>Copper Lantern — Business Card</title>
<link href="https://fonts.googleapis.com/css2?family=Arimo:wght@400;700&display=swap" rel="stylesheet">
<style>
  :root {
    --page-bg: #e6e6e6;
    --card-edge: #0b2638;
    --card-mid: #124d72;
    --card-glow: #1d8fdc;
    --band: #050b10;
    --name: #e2f3ff;
    --tagline: #e6ff1a;
    --contact: #ffffff;
    --divider: #ffffff;
    --mark: #e2f3ff;
  }
  html, body {
    margin: 0;
    width: 1200px;
    height: 801px;
    overflow: hidden;
    background: var(--page-bg);
  }
  .business-card {
    position: absolute;
    left: 40px;
    top: 76px;
    width: 1120px;
    height: 648px;
    border-radius: 40px;
    overflow: hidden;
    font-family: "Arimo", Arial, sans-serif;
    background:
      radial-gradient(ellipse 30% 62% at 50% 78%, rgba(40,160,235,0.95) 0%, rgba(25,120,190,0.55) 45%, rgba(18,77,114,0) 100%),
      radial-gradient(ellipse 55% 75% at 50% 40%, var(--card-mid) 0%, var(--card-edge) 100%);
  }
  .brand-mark {
    position: absolute;
    left: 528px;
    top: 168px;
    width: 64px;
    height: 64px;
    border-radius: 50%;
    background: var(--mark);
  }
  .brand-name {
    position: absolute;
    left: 0;
    width: 100%;
    top: 278px;
    text-align: center;
    font-size: 31px;
    line-height: 36px;
    font-weight: 400;
    letter-spacing: 0.27em;
    text-indent: 0.27em;
    color: var(--name);
    text-transform: uppercase;
  }
  .tagline {
    position: absolute;
    left: 0;
    width: 100%;
    top: 321px;
    text-align: center;
    font-size: 26px;
    line-height: 32px;
    font-weight: 400;
    color: var(--tagline);
  }
  .contact-band {
    position: absolute;
    left: 0;
    bottom: 0;
    width: 100%;
    height: 176px;
    background: var(--band);
  }
  .address-block {
    position: absolute;
    left: 71px;
    top: 56px;
    font-size: 20px;
    font-weight: 700;
    line-height: 42px;
    color: var(--contact);
    white-space: nowrap;
  }
  .band-divider {
    position: absolute;
    left: 630px;
    top: 44px;
    width: 2px;
    height: 100px;
    background: var(--divider);
  }
  .web-address {
    position: absolute;
    left: 705px;
    top: 84px;
    font-size: 25px;
    line-height: 32px;
    font-weight: 700;
    color: var(--contact);
    white-space: nowrap;
  }
</style>
</head>
<body>
  <div class="business-card">
    <div class="brand-mark"></div>
    <div class="brand-name">Copper Lantern</div>
    <div class="tagline">finest quality audio mastering</div>
    <div class="contact-band">
      <div class="address-block">
        718 - 42nd Avenue N.W. Redmere, Ontario, Canada<br>
        K7L 2R5&nbsp; Telephone: (555) 318 - 6042
      </div>
      <div class="band-divider"></div>
      <div class="web-address">Web: www.copperlantern.ca</div>
    </div>
  </div>
</body>
</html>
```